Label for Custom Gin Botle

Design an label for Gin botle, need label asap sorry

Target Market(s)

Our customers

Requirements
Must have
• Classic/expensive look

```html
<!DOCTYPE html>
<html lang="nl">
<head>
<meta charset="utf-8">
<title>Carvers Gin – Label</title>
<link rel="stylesheet" href="https://fonts.googleapis.com/css2?family=Alfa+Slab+One&family=Oswald:wght@400;500;600&family=Roboto+Slab:wght@500&display=swap">
<style>
  :root {
    --backdrop: #2e8535;
    --label-green: #2f9a3a;
    --label-green-deep: #23782c;
    --ink: #1a1a1a;
    --paper: #f2f2f2;
    --glass-light: #d7ecd6;
    --glass-mid: #8cc58f;
  }
  html, body {
    margin: 0;
    padding: 0;
    width: 1200px;
    height: 836px;
    overflow: hidden;
    background: var(--backdrop);
  }
  .canvas {
    position: relative;
    width: 1200px;
    height: 836px;
    background: var(--backdrop);
  }
  .gin-label {
    position: absolute;
    left: 397px;
    top: 73px;
    width: 405px;
    height: 689px;
  }
  .frame-paper { fill: var(--paper); }
  .frame-field { fill: var(--label-green); }
  .frame-rule { fill: none; stroke: var(--ink); stroke-width: 3; }
  .frame-rule-thin { fill: none; stroke: var(--ink); stroke-width: 1.5; }
  .stamp-disc { fill: var(--paper); }
  .stamp-word {
    font-family: "Oswald", sans-serif;
    font-weight: 500;
    font-size: 22px;
    letter-spacing: 5px;
    fill: var(--label-green);
  }
  .crest-area { fill: var(--ink); }
  .maker-plate { fill: var(--ink); }
  .maker-name {
    font-family: "Oswald", sans-serif;
    font-weight: 600;
    font-size: 38px;
    letter-spacing: 2px;
    fill: var(--paper);
  }
  .title-banner { fill: var(--ink); }
  .banner-rule { fill: none; stroke: var(--paper); stroke-width: 3; }
  .title-word {
    font-family: "Alfa Slab One", serif;
    fill: var(--paper);
  }
  .title-diamond { fill: var(--label-green); }
  .vintage-year {
    font-family: "Roboto Slab", serif;
    font-weight: 500;
    font-size: 22px;
    letter-spacing: 2px;
    fill: var(--paper);
  }
  .vintage-pad { fill: var(--ink); }
  .wave-rule { fill: none; stroke: var(--ink); stroke-width: 3; }
  .glass-area { fill: url(#glassTone); }
  .info-text {
    font-family: "Oswald", sans-serif;
    font-weight: 500;
    fill: var(--ink);
  }
  .info-small { font-size: 22px; }
  .info-mid { font-size: 30px; }
  .info-large { font-size: 48px; }
</style>
</head>
<body>
<main class="canvas">
  <svg class="gin-label" viewBox="0 0 775 1318" xmlns="http://www.w3.org/2000/svg" role="group" aria-label="Carvers Gin label">
    <defs>
      <linearGradient id="glassTone" x1="0" y1="0" x2="0" y2="1">
        <stop offset="0" stop-color="var(--glass-light)"/>
        <stop offset="0.55" stop-color="var(--glass-mid)"/>
        <stop offset="1" stop-color="var(--glass-light)"/>
      </linearGradient>
      <path id="batchArc" d="M 124,180 A 44 44 0 0 1 212,180"/>
      <path id="bottleArc" d="M 539,180 A 44 44 0 0 1 627,180"/>
    </defs>

    <!-- label frames -->
    <path class="frame-paper" d="M45,0 H730 A45 45 0 0 0 775 45 V1273 A45 45 0 0 0 730 1318 H45 A45 45 0 0 0 0 1273 V45 A45 45 0 0 0 45 0 Z"/>
    <path class="frame-field" d="M55,20 H720 A35 35 0 0 0 755 55 V1263 A35 35 0 0 0 720 1298 H55 A35 35 0 0 0 20 1263 V55 A35 35 0 0 0 55 20 Z"/>
    <path class="frame-rule" d="M68,38 H707 A30 30 0 0 0 737 68 V1250 A30 30 0 0 0 707 1280 H68 A30 30 0 0 0 38 1250 V68 A30 30 0 0 0 68 38 Z"/>
    <path class="frame-rule-thin" d="M74,50 H701 A24 24 0 0 0 725 74 V1244 A24 24 0 0 0 701 1268 H74 A24 24 0 0 0 50 1244 V74 A24 24 0 0 0 74 50 Z"/>

    <!-- batch / bottle stamps -->
    <circle class="stamp-disc" cx="168" cy="178" r="70"/>
    <circle class="stamp-disc" cx="583" cy="178" r="70"/>
    <text class="stamp-word"><textPath href="#batchArc" startOffset="50%" text-anchor="middle">BATCH</textPath></text>
    <text class="stamp-word"><textPath href="#bottleArc" startOffset="50%" text-anchor="middle">BOTTLE</textPath></text>

    <!-- crest -->
    <circle class="crest-area" cx="387" cy="172" r="55" role="img" aria-label="Distillery crest emblem"/>

    <!-- title banner -->
    <path class="title-banner" d="M-5,390 Q387,200 780,390 L780,610 Q387,890 -5,610 Z"/>
    <path class="banner-rule" d="M15,402 Q387,222 760,402 L760,600 Q387,866 15,600 Z"/>
    <path class="banner-rule" d="M58,600 Q387,470 717,600"/>
    <polygon class="title-diamond" points="130,618 185,604 240,618 185,632"/>
    <polygon class="title-diamond" points="530,618 585,604 640,618 585,632"/>

    <text class="title-word" x="387" y="505" font-size="140" text-anchor="middle" textLength="600" lengthAdjust="spacingAndGlyphs">CARVERS</text>
    <text class="title-word" x="387" y="700" font-size="160" text-anchor="middle" textLength="245" lengthAdjust="spacingAndGlyphs">GIN</text>

    <rect class="vintage-pad" x="352" y="722" width="70" height="26"/>
    <text class="vintage-year" x="387" y="743" text-anchor="middle">2024</text>

    <!-- maker plate -->
    <rect class="maker-plate" x="262" y="192" width="256" height="113" rx="16"/>
    <text class="maker-name" x="390" y="264" text-anchor="middle">VELDMAN</text>

    <!-- lower panel -->
    <path class="wave-rule" d="M38,790 C160,760 260,830 387,825 C520,820 620,760 737,790"/>
    <line class="frame-rule" x1="58" y1="815" x2="58" y2="1240"/>
    <line class="frame-rule" x1="717" y1="825" x2="717" y2="1240"/>

    <text class="info-text info-mid" x="180" y="962" text-anchor="middle">VELDMAN GIN</text>
    <text class="info-text info-mid" x="585" y="962" text-anchor="middle">EST. 2021</text>

    <rect class="glass-area" x="295" y="895" width="185" height="195" rx="10" role="img" aria-label="Gin tumbler with ice"/>

    <line class="frame-rule" x1="70" y1="1112" x2="705" y2="1112"/>
    <line class="frame-rule" x1="278" y1="1132" x2="278" y2="1235"/>
    <line class="frame-rule" x1="485" y1="1132" x2="485" y2="1235"/>

    <text class="info-text info-small" x="78" y="1172">KAN SPOREN VAN</text>
    <text class="info-text info-small" x="78" y="1204">ALLERGENEN BEVATTEN</text>
    <text class="info-text info-large" x="383" y="1202" text-anchor="middle">40% VOL</text>
    <text class="info-text info-large" x="603" y="1202" text-anchor="middle">500ML</text>
  </svg>
</main>
</body>
</html>
```